Halvorsen Electric service department flyer

Looking to design a electrical service department flyer. The company has been in San Francisco for 60yrs primarily doing work in the downtown area. https://halvorsenelectric.example/about-halvorsen/
I attached a rough draft of the flyer. I would like to see something with the san francisco downtown skyline watermarked on the front page, open to the second page that describes all services and contact.

```html
<!DOCTYPE html>
<html lang="en">
<head>
<meta charset="utf-8">
<title>Halvorsen Electric – Service Department Flyer</title>
<link href="https://fonts.googleapis.com/css2?family=Rubik:wght@400;500;600;700&family=Roboto:wght@400;500&display=swap" rel="stylesheet">
<style>
  :root{
    --stage:#9c9c9c;
    --navy:#0c3d8f;
    --brand:#1450a8;
    --sky:#1e9ad8;
    --ink:#2b2f36;
    --paper:#f4f8fd;
    --pale:#dcebf8;
    --panel:#d5e7f7;
    --green:#29a844;
    --footer:#141414;
    --white:#ffffff;
  }
  *{box-sizing:border-box;margin:0;padding:0}
  html,body{width:1200px;height:765px;overflow:hidden}
  body{background:var(--stage);font-family:"Roboto",Arial,sans-serif;color:var(--ink);position:relative}
  .page{position:absolute;overflow:hidden;background:linear-gradient(160deg,var(--white) 0%,var(--paper) 45%,var(--pale) 100%)}
  .page--front{left:52px;top:43px;width:528px;height:683px}
  .page--back{left:615px;top:43px;width:530px;height:685px}

  .skyline{position:absolute;left:0;top:0;width:100%;background:linear-gradient(180deg,#1a3f8a 0%,#2a56a8 55%,#3a68b6 100%)}
  .page--front .skyline{height:260px}
  .page--back .skyline{height:222px}

  .brand{position:absolute;left:34px;top:38px;color:var(--white)}
  .brand__name{font-family:"Rubik",Arial,sans-serif;font-weight:700;font-size:27px;line-height:30px;letter-spacing:.5px;text-transform:uppercase}
  .brand__tag{font-family:"Rubik",Arial,sans-serif;font-weight:600;font-size:12px;letter-spacing:.6px;margin-top:46px}

  .front-panel{position:absolute;left:0;top:157px;width:300px;height:160px;background:#eef5fc;border-top-right-radius:60px}
  .front-body{position:absolute;left:0;top:260px;width:100%;height:370px;background:linear-gradient(180deg,#eef5fc 0%,#e2eef9 100%)}

  .collage{position:absolute;left:242px;top:14px}

  .welcome{position:absolute;left:34px;top:180px;width:300px;z-index:1}
  .welcome__title{font-family:"Rubik",Arial,sans-serif;font-weight:600;font-size:23px;line-height:31px;color:var(--brand);white-space:nowrap}
  .welcome__text{font-size:11.1px;line-height:14.4px;margin-top:10px;color:#333;white-space:nowrap}

  .photo{position:absolute;border:2px solid var(--sky);border-radius:14px;overflow:hidden}
  .photo--home{left:32px;top:375px;width:216px;height:93px;background:linear-gradient(135deg,#1d2f4c 0%,#4f6b7e 40%,#d9d6cf 70%,#8a5a3c 100%)}
  .photo--office{left:280px;top:375px;width:216px;height:93px;background:linear-gradient(90deg,#cfd6de 0%,#3c4350 45%,#6b5a34 75%,#e5b640 100%)}

  .service{position:absolute;top:476px;width:240px}
  .service--res{left:38px}
  .service--com{left:288px}
  .service__title{font-family:"Rubik",Arial,sans-serif;font-weight:600;font-size:15px;color:var(--brand);margin-bottom:6px}
  .bolt-list{list-style:none}
  .bolt-list li{font-size:10.4px;line-height:17px;padding-left:12px;position:relative;white-space:nowrap}
  .bolt-list li::before{content:"";position:absolute;left:0;top:4px;width:7px;height:10px;background:var(--brand);clip-path:polygon(60% 0,10% 55%,45% 55%,30% 100%,90% 40%,55% 40%)}

  .rule{position:absolute;left:0;width:100%;height:3px;background:var(--brand)}
  .page--front .rule{top:624px}
  .page--back .rule{top:627px}
  .footer{position:absolute;left:0;width:100%;background:var(--footer);display:flex;align-items:center;justify-content:center;gap:12px;color:var(--white);font-size:10.6px;white-space:nowrap}
  .page--front .footer{top:629px;height:54px}
  .page--back .footer{top:632px;height:53px}
  .contact{display:flex;align-items:center;gap:5px;white-space:nowrap;flex:none}
  .contact svg{width:20px;height:20px;flex:none}

  /* back page */
  .back-panel{position:absolute;left:0;top:175px;width:200px;height:60px;background:#f6f9fd;border-top-right-radius:40px}
  .back-body{position:absolute;left:0;top:222px;width:100%;height:405px;background:linear-gradient(160deg,#f6f9fd 0%,#e8f1fa 60%,#dbe9f7 100%)}
  .why{position:absolute;left:37px;top:232px;font-family:"Rubik",Arial,sans-serif;font-weight:700;font-size:22.5px;line-height:28px;color:var(--brand)}
  .reasons{position:absolute;left:36px;top:300px;list-style:none}
  .reason{display:flex;align-items:center;gap:7px;height:38px;margin-bottom:8px;font-size:12px;line-height:15px}
  .reason:nth-child(3){height:46px}
  .reason b{font-weight:500}
  .ring{width:38px;height:38px;border:1.5px solid var(--brand);border-radius:50%;flex:none;display:flex;align-items:center;justify-content:center}
  .ring svg{width:22px;height:22px}

  .pill{position:absolute;left:223px;top:271px;width:263px;height:30px;border-radius:15px;background:var(--brand);color:var(--white);font-family:"Rubik",Arial,sans-serif;font-weight:600;font-size:19.5px;display:flex;align-items:center;justify-content:center}
  .sectors{position:absolute;left:220px;top:318px;width:290px;display:flex}
  .sector{width:96.6px;text-align:center;font-size:10.5px;font-weight:500;line-height:13px}
  .sector + .sector{border-left:1px dotted var(--brand)}
  .sector__badge{width:50px;height:50px;margin:2px auto 6px;border-radius:50%;border:2px solid var(--brand);border-right-color:#222;display:flex;align-items:center;justify-content:center}
  .sector__badge svg{width:30px;height:30px}

  .offer-box{position:absolute;left:217px;top:410px;width:290px;height:72px;background:var(--panel);border:1px solid #b9d4ee;border-radius:16px;display:grid;grid-template-columns:124px 1fr;padding:12px 0 0 18px}
  .offer-box .bolt-list li{font-size:11.8px;line-height:15.3px}

  .contact-bar{position:absolute;left:37px;top:509px;width:464px;height:85px;background:var(--brand);border-radius:22px;color:var(--white);display:flex;align-items:center;padding-left:32px}
  .contact-bar__item{display:flex;align-items:center;gap:8px}
  .contact-bar__item + .contact-bar__item{margin-left:22px}
  .contact-bar__icon{width:46px;height:46px;border:1.5px solid var(--white);border-radius:50%;display:flex;align-items:center;justify-content:center;flex:none}
  .contact-bar__icon svg{width:26px;height:26px}
  .contact-bar__label{font-family:"Rubik",Arial,sans-serif;font-weight:600;font-size:13.5px}
  .contact-bar__value{font-size:13.5px;line-height:17px;white-space:nowrap}
</style>
</head>
<body>

<section class="page page--front">
  <div class="skyline" role="img" aria-label="Downtown San Francisco skyline at dusk, tinted blue"></div>
  <div class="brand">
    <div class="brand__name">Halvorsen<br>Electric</div>
    <div class="brand__tag">ELECTRICAL / DATACOM</div>
  </div>
  <div class="front-panel"></div>
  <div class="front-body"></div>

  <svg class="collage" width="340" height="340" viewBox="0 0 340 340">
    <defs>
      <linearGradient id="ringGrad" x1="0" y1="0" x2="1" y2="1">
        <stop offset="0" stop-color="#1ea4e0"/>
        <stop offset="1" stop-color="#0e4a9e"/>
      </linearGradient>
      <radialGradient id="photoGrad" cx=".5" cy=".5" r=".6">
        <stop offset="0" stop-color="#8a7a6a"/>
        <stop offset=".6" stop-color="#3a3f55"/>
        <stop offset="1" stop-color="#1c2540"/>
      </radialGradient>
    </defs>
    <circle cx="170" cy="170" r="168" fill="url(#ringGrad)"/>
    <circle cx="175" cy="170" r="132" fill="url(#photoGrad)" role="img" aria-label="Collage of interior and building lighting projects"/>
    <g stroke="#ffffff" stroke-width="4">
      <line x1="175" y1="170" x2="210" y2="38"/>
      <line x1="175" y1="170" x2="60" y2="110"/>
      <line x1="175" y1="170" x2="70" y2="255"/>
      <line x1="175" y1="170" x2="190" y2="302"/>
      <line x1="175" y1="170" x2="306" y2="190"/>
    </g>
    <circle cx="168" cy="213" r="58" fill="var(--green)" stroke="#1ea4e0" stroke-width="3"/>
    <text x="168" y="195" text-anchor="middle" font-family="Rubik, sans-serif" font-weight="600" font-size="17" fill="#fff">Free</text>
    <text x="168" y="218" text-anchor="middle" font-family="Rubik, sans-serif" font-weight="600" font-size="17" fill="#fff">Estimate</text>
    <text x="168" y="241" text-anchor="middle" font-family="Rubik, sans-serif" font-weight="600" font-size="17" fill="#fff">Available</text>
  </svg>

  <div class="welcome">
    <h1 class="welcome__title">Welcome to<br>Halvorsen Electric</h1>
    <p class="welcome__text">Halvorsen Electric is a licensed<br>electrical contractor proudly,<br>serving San Francisco and surrounding<br>Bay Area communities. our experienced<br>electricians provide safe, efficient, and<br>code-compliant electrical solutions for residential<br>and commercial properties.</p>
  </div>

  <div class="photo photo--home" role="img" aria-label="Modern home exterior lit at dusk"></div>
  <div class="photo photo--office" role="img" aria-label="Commercial lobby with mailboxes and warm wall lighting"></div>

  <div class="service service--res">
    <h2 class="service__title">Residential Electrical</h2>
    <ul class="bolt-list">
      <li>Electrical repairs &amp; troubleshooting</li>
      <li>Panel upgrades &amp; breaker replacement Lighting</li>
      <li>installation (indoor &amp; outdoor)</li>
      <li>EV charger installation</li>
      <li>Rewiring &amp; remodels</li>
      <li>Emergency electrical services</li>
    </ul>
  </div>
  <div class="service service--com">
    <h2 class="service__title">Commercial Electrical</h2>
    <ul class="bolt-list">
      <li>Office &amp; retail electrical systems</li>
      <li>Lighting upgrades &amp; maintenance Electrical</li>
      <li>inspections</li>
      <li>Tenant improvements</li>
      <li>Emergency electrical services</li>
    </ul>
  </div>

  <div class="rule"></div>
  <footer class="footer">
    <span class="contact"><svg viewBox="0 0 24 24" fill="none" stroke="#fff" stroke-width="1.2"><circle cx="12" cy="12" r="11"/><rect x="6.5" y="8" width="11" height="8"/><path d="M6.5 8l5.5 4.5L17.5 8"/></svg>info@halvorsenelectric.example</span>
    <span class="contact"><svg viewBox="0 0 24 24" fill="none" stroke="#fff" stroke-width="1.2"><circle cx="12" cy="12" r="11"/><path d="M8.5 6.5l2 2.5-1.2 1.4c.8 1.8 2 3 3.8 3.8l1.4-1.2 2.5 2-1.2 1.8c-4.5-.3-8.3-4.1-8.6-8.6z" fill="#fff"/></svg>415-555-0142</span>
    <span class="contact"><svg viewBox="0 0 24 24" fill="none" stroke="#fff" stroke-width="1.2"><circle cx="12" cy="12" r="11"/><circle cx="12" cy="12" r="6"/><ellipse cx="12" cy="12" rx="2.6" ry="6"/><path d="M6 12h12"/></svg>www.halvorsenelectric.example</span>
  </footer>
</section>

<section class="page page--back">
  <div class="skyline" role="img" aria-label="San Francisco downtown skyline with bay bridge, tinted blue"></div>
  <div class="brand">
    <div class="brand__name">Halvorsen<br>Electric</div>
    <div class="brand__tag">ELECTRICAL / DATACOM</div>
  </div>
  <div class="back-panel"></div>
  <div class="back-body"></div>

  <h2 class="why">WHY<br>CHOOSE US</h2>
  <ul class="reasons">
    <li class="reason"><span class="ring"><svg viewBox="0 0 24 24" fill="none" stroke="#1450a8" stroke-width="1.4"><circle cx="12" cy="8" r="3.5"/><path d="M5 20c1-4 4-6 7-6s6 2 7 6"/></svg></span><span><b>Customer service</b><br>is our priority</span></li>
    <li class="reason"><span class="ring"><svg viewBox="0 0 24 24" fill="none" stroke="#1450a8" stroke-width="1.4"><circle cx="14" cy="9" r="6"/><path d="M15.5 6.5h-2.5a1.2 1.2 0 000 2.5h2a1.2 1.2 0 010 2.5h-2.5M14 5v8"/><path d="M3 21v-6h3v6zM6 15l3-3 2 1"/></svg></span><span><b>Honest pricing</b> &amp;<br>dependable results</span></li>
    <li class="reason"><span class="ring"><svg viewBox="0 0 24 24" fill="none" stroke="#1450a8" stroke-width="1.4"><path d="M4 21h16M7 21v-5h4v5M11 21v-9h4v9"/><path d="M14 12V3l5 2-5 2"/></svg></span><span>San Francisco<br>based company<br><b>since 1966</b></span></li>
    <li class="reason"><span class="ring"><svg viewBox="0 0 24 24" fill="none" stroke="#1450a8" stroke-width="1.4"><circle cx="9" cy="10" r="5"/><circle cx="9" cy="10" r="2"/><circle cx="17" cy="17" r="3.5"/><path d="M17 15.5v1.5l1 1"/></svg></span><span>Professional, clean<br>and <b>efficient work</b></span></li>
  </ul>

  <div class="pill">Free Estimate Available</div>

  <div class="sectors">
    <div class="sector">
      <div class="sector__badge"><svg viewBox="0 0 30 30" fill="none" stroke="#1450a8" stroke-width="1.4"><path d="M3 26h24M5 26V14l6-5 6 5v12M17 26V6h9v20"/><rect x="8.5" y="18" width="5" height="8"/><path d="M19.5 10h4M19.5 14h4M19.5 18h4"/></svg></div>
      Residential
    </div>
    <div class="sector">
      <div class="sector__badge"><svg viewBox="0 0 30 30" fill="none" stroke="#1450a8" stroke-width="1.4"><path d="M3 26h24M6 26V10h8v16M14 26V4h10v22"/><path d="M8.5 14h3M8.5 18h3M8.5 22h3M17 8h4M17 12h4M17 16h4M17 20h4"/></svg></div>
      Commercial
    </div>
    <div class="sector">
      <div class="sector__badge"><svg viewBox="0 0 30 30" fill="none" stroke="#1450a8" stroke-width="1.4"><circle cx="15" cy="15" r="11"/><text x="15" y="18" text-anchor="middle" font-family="Roboto, sans-serif" font-size="8" fill="#1450a8" stroke="none">24/7</text></svg></div>
      24/7 Emergency<br>Service
    </div>
  </div>

  <div class="offer-box">
    <ul class="bolt-list">
      <li>Electrical Repairs</li>
      <li>Panel Upgrades</li>
      <li>TI Upgrades</li>
    </ul>
    <ul class="bolt-list">
      <li>Lighting Installation</li>
      <li>Building maintenance</li>
      <li>EV Charger Installation</li>
    </ul>
  </div>

  <div class="contact-bar">
    <div class="contact-bar__item">
      <span class="contact-bar__icon"><svg viewBox="0 0 24 24"><path d="M6 3.5l3.5 4.2-2 2.3c1.4 3 3.4 5 6.4 6.4l2.3-2 4.2 3.5-2 3C10.6 20.3 3.7 13.4 3 5.5z" fill="#fff"/></svg></span>
      <div><div class="contact-bar__label">Phone</div><div class="contact-bar__value">415-555-0142</div></div>
    </div>
    <div class="contact-bar__item">
      <span class="contact-bar__icon"><svg viewBox="0 0 24 24" fill="none" stroke="#fff" stroke-width="1.6"><circle cx="12" cy="12" r="8"/><path d="M12 7v5.5l-2.5 1.5"/></svg></span>
      <div><div class="contact-bar__label">Hourse</div><div class="contact-bar__value">Mon-Fri: 8.00AM - 5:00 PM<br>Emergency Service Available</div></div>
    </div>
  </div>

  <div class="rule"></div>
  <footer class="footer">
    <span class="contact"><svg viewBox="0 0 24 24" fill="none" stroke="#fff" stroke-width="1.2"><circle cx="12" cy="12" r="11"/><rect x="6.5" y="8" width="11" height="8"/><path d="M6.5 8l5.5 4.5L17.5 8"/></svg>info@halvorsenelectric.example</span>
    <span class="contact"><svg viewBox="0 0 24 24" fill="none" stroke="#fff" stroke-width="1.2"><circle cx="12" cy="12" r="11"/><path d="M8.5 6.5l2 2.5-1.2 1.4c.8 1.8 2 3 3.8 3.8l1.4-1.2 2.5 2-1.2 1.8c-4.5-.3-8.3-4.1-8.6-8.6z" fill="#fff"/></svg>415-555-0142</span>
    <span class="contact"><svg viewBox="0 0 24 24" fill="none" stroke="#fff" stroke-width="1.2"><circle cx="12" cy="12" r="11"/><circle cx="12" cy="12" r="6"/><ellipse cx="12" cy="12" rx="2.6" ry="6"/><path d="M6 12h12"/></svg>www.halvorsenelectric.example</span>
  </footer>
</section>

</body>
</html>
```